vermalo web design

- Company / Site Description
We are developing a website that will allow anyone in Europe to find in one click, cultural things to do (Exhibition, Museum, Monument, Zoo, Aquarium, Archaeological site…) with friends or family, and to organize the visit (book a ticket / a private visit, book a restaurant nearby…).

Examples
1. You're in London with your girlfriend, it's saturday 10 am, you have two hours to spend and you want to see an exhibition. We provide you in one click all the exhibition matching your location / time and date.

2. You're in Berlin with some friends, it's thursday night you want to go out, but you don't know what to do. We provide you a list of experience, you can select for instance "I want to be on top of the world", and we show you a list of venues matching the selected experience / date / time /location of your request.

- Brand name : Vermalo
- Activity : Cultural Leisure, cultural entertainment

- Target audience
Broad target will be between 20 and 55. Core target will be between 25 and 40. Most likely to live in a city and in Europe.

- Behaviours and preferences
Our user is under time constraint (few minutes to find and choose his visit), idea constraint (is not sure about what to do and see) and money constraint.
He wants to have an easy to use website, not cluttered with information, focussed on added value information. He wants to have a website which is modern, fun and elegant that he will deem as professional and trustworthy.

- Our expectations (Do’s and Don’t)
We want to move away from traditional design. We want some OUT OF THE BOX design. Think of a website design that will look like an app design.
We want to make an awesome / extra ordinary /remember-able design. The design must be so cool, that the user wants to come back to the site. In two words: THINK EXTRAORDINARY.
You can use photos to help the user understand functions. If you use photo, use creative commons license photo.
Avoid black colors

- Functional Requirements
We need Four pages:
1. Home Page (desktop and mobile version): it’s both the homepage and the assistant page. This page will allow the user to find in one click his visit (please refer to the pdf file Assistant home page). The page must be self-explanatory for a first time user.
2. Assistant result page (desktop version): it’s the page that display the results found by the assistant based on the criteria search (please refer to the pdf file mockup - Assistant result page)
3. Site / Event page (desktop version): it’s the page that display each result information (please refer to the pdf file mockup – Event / Site Page)
The pdf files list all the elements include in each page + gives you a mockup of each page (just to put in perspective the element required). You are completely free about the design.
We don’t have the logo yet. Use a dummy logo for your page design.
The selected winner can expect to work with us immediately after the contest and on a on a regular basis later on.

- Technical Requirements
No Flash
For the winner, we will manage the CSS you will just need to provide :
. One PSD file containing all the pages
. Inside the PSD file we want for each page two groups: the first group will embed the desktop design, the second group will embed the responsive mobile design (Home Page only).
In total there should be 4 groups inside the PSD file (3 desktop groups, 1 mobile group).
Each group must contain all the elements specified in the pdf file

Website we like
http://demo.plandorix.example/?theme=Velunt
http://rosabel.quintorhub.example/#home
http://blogsite.fenk.daltoroute.example/2/
http://demo.plandorix.example/?theme=Mosaru
http://www.quarnivo.example/themes/lumbe/
http://gridmarket.example/item/tav-responsive-photography-blog-theme/full_screen_preview/8146027
http://items.zkvortel.example/?product=example
http://uk.harnoway.example

Reason: Due to the request of several designers, we have agreed to add 7 additional days to the contest deadline. Thank you. The vermalo team

Reason: We still need to collect all the votes. Sorry for the delay.

Reason: Hello, We extend the contest deadline, in order to collect all the votes from the poll. We should have everything finalized by sunday. Thank you vermalo team

```html
<!DOCTYPE html>
<html lang="en">
<head>
<meta charset="utf-8">
<title>Vermalo – My Assistant</title>
<link rel="stylesheet" href="https://fonts.googleapis.com/css2?family=Raleway:wght@200;300&family=Montserrat:wght@400;500;600;700&display=swap">
<style>
  :root{
    --bar:#2a292e;
    --coral:#fb7a6c;
    --coral-deep:#f86b60;
    --ink:#3b3270;
    --white:#ffffff;
    --grey-text:#c9c8cd;
    --row-date:#ffffff;
    --row-time:#fdf3c0;
    --row-place:#fde0a3;
    --row-want:#fdb18c;
    --tick:#a49fb0;
    --lang:#f7a688;
  }
  *{box-sizing:border-box;margin:0;padding:0}
  html,body{width:1200px;height:954px;overflow:hidden}
  body{position:relative;font-family:"Montserrat",sans-serif;background:var(--white)}

  .top-bar{position:absolute;left:0;top:0;width:1200px;height:41px;background:var(--bar)}
  .tab{position:absolute;top:0;height:41px;line-height:44px;font-size:12px;letter-spacing:.5px;text-transform:uppercase}
  .tab--active{left:162px;width:212px;background:var(--coral);color:#2a292e;font-weight:600;text-align:center}
  .tab--active::after{content:"";position:absolute;left:94px;top:41px;border:8px solid transparent;border-top:8px solid var(--coral);border-bottom:0}
  .tab--fav{left:440px;color:var(--grey-text)}
  .search{position:absolute;left:860px;top:12px;font-size:12px;color:var(--grey-text)}
  .search svg{position:absolute;left:56px;top:0}
  .divider{position:absolute;left:947px;top:0;width:1px;height:41px;background:#4a494f}
  .login{position:absolute;left:966px;top:12px;font-size:12px;color:var(--grey-text)}
  .login svg{position:absolute;left:48px;top:-5px}

  .assistant-side{position:absolute;left:0;top:41px;width:600px;height:870px;background:var(--white)}
  .headline{position:absolute;right:23px;top:60px;font-family:"Raleway",sans-serif;font-weight:200;font-size:46px;letter-spacing:-1.5px;color:#222;white-space:nowrap;line-height:56px}
  .headline strong{font-family:"Montserrat",sans-serif;font-weight:400;color:var(--coral);letter-spacing:-0.5px}
  .subline{position:absolute;right:26px;top:117px;font-size:14px;color:#333;white-space:nowrap}
  .pitch{position:absolute;right:20px;top:148px;font-size:12.5px;font-weight:700;color:var(--coral);letter-spacing:.3px;white-space:nowrap}

  .photo{position:absolute}
  .photo--statue{left:163px;top:221px;width:206px;height:167px;background:linear-gradient(160deg,#d9dde6,#9aa2b6)}
  .photo--tiger{left:163px;top:388px;width:206px;height:109px;background:linear-gradient(90deg,#10103a 40%,#8d8a95)}
  .photo--carousel{left:163px;top:497px;width:206px;height:153px;background:linear-gradient(160deg,#d6a2ae,#8a4a6a 60%,#e6c7b8)}
  .photo--tower{left:369px;top:221px;width:232px;height:464px;background:linear-gradient(180deg,#19183e 0%,#2b2a66 45%,#7a6a3a 70%,#2b3a2a 100%)}

  .planner-side{position:absolute;left:600px;top:41px;width:600px;height:870px;background:radial-gradient(circle at 65% 45%,#6e5a7e 0%,transparent 45%),linear-gradient(180deg,#8c7896 0%,#5f4c78 45%,#2e2c5c 80%,#25285a 100%);box-shadow:inset 3px 0 4px rgba(0,0,0,.35)}

  .weather{position:absolute;left:970px;top:88px;color:var(--white);text-align:center;width:68px}
  .weather svg{display:block;margin:0 auto}
  .weather__temp{font-size:33px;font-weight:700;line-height:1;margin-top:2px}
  .weather__temp span{font-weight:300;font-size:28px}

  .criterion{position:absolute;left:663px;height:76px;display:flex;box-shadow:0 1px 3px rgba(0,0,0,.3)}
  .criterion__mark{width:72px;border-right:1px solid rgba(0,0,0,.15);display:flex;align-items:center;justify-content:center}
  .criterion__value{display:flex;align-items:center;padding-left:23px;color:var(--ink);font-size:19px;text-transform:uppercase}
  .criterion__value b{font-weight:700;margin-right:6px}
  .criterion--date{top:266px;width:377px;background:var(--row-date)}
  .criterion--time{top:342px;width:281px;background:var(--row-time)}
  .criterion--time .criterion__value{font-size:32px;font-weight:400;padding-left:27px}
  .criterion--place{top:417px;width:342px;background:var(--row-place)}
  .criterion--place .criterion__value{padding-top:10px}
  .criterion--want{top:493px;width:377px;height:75px;background:var(--row-want)}
  .criterion--want .criterion__value{padding-left:27px;padding-top:7px}
  .question{font-size:22px;font-weight:700;color:#8a5a6a}

  .go{position:absolute;left:971px;top:595px;width:72px;height:72px;border-radius:50%;background:var(--coral-deep);color:#4a2a40;font-weight:700;font-size:18px;display:flex;align-items:center;justify-content:center;box-shadow:0 2px 4px rgba(0,0,0,.35)}
  .go svg{margin-left:4px}

  .bottom-bar{position:absolute;left:0;top:911px;width:1200px;height:43px;background:var(--bar);color:var(--white);font-size:12.5px}
  .language{position:absolute;left:88px;top:11px}
  .language b{color:var(--lang);margin-left:8px;font-weight:700}
  .plus{position:absolute;left:984px;top:14px}
  .plus svg{margin-left:4px}
</style>
</head>
<body>
  <header class="top-bar">
    <div class="tab tab--active">My Assistant</div>
    <div class="tab tab--fav">My Favourites</div>
    <div class="search">search
      <svg width="18" height="16" viewBox="0 0 18 16"><circle cx="6" cy="6" r="4.2" fill="none" stroke="#d8d7dc" stroke-width="2"/><line x1="9" y1="9" x2="15" y2="14" stroke="#d8d7dc" stroke-width="2.5" stroke-linecap="round"/></svg>
    </div>
    <div class="divider"></div>
    <div class="login">login
      <svg width="25" height="25" viewBox="0 0 25 25"><circle cx="12.5" cy="12.5" r="11" fill="none" stroke="#fff" stroke-width="2"/><circle cx="12.5" cy="9.5" r="4" fill="#fff"/><path d="M5 19c2-4 13-4 15 0" fill="#fff"/></svg>
    </div>
  </header>

  <section class="assistant-side">
    <h1 class="headline">FIND IN <strong>ONE</strong> CLICK</h1>
    <p class="subline">Exhibitions, museums, monuments, zoos...</p>
    <p class="pitch">TELL US WHAT YOU LIKE, WE WILL TELL YOU WHERE TO GO!</p>
    <div class="photo photo--statue" role="img" aria-label="Marble sculpture of two embracing figures"></div>
    <div class="photo photo--tiger" role="img" aria-label="White tiger in black and white"></div>
    <div class="photo photo--carousel" role="img" aria-label="Children riding a carousel near the Eiffel Tower"></div>
    <div class="photo photo--tower" role="img" aria-label="Illuminated Eiffel Tower at night with fountains"></div>
  </section>

  <section class="planner-side" role="img" aria-label="Blurred evening city lights in purple tones"></section>

  <div class="weather">
    <svg width="60" height="56" viewBox="4 2 52 44"><g stroke="#fff" stroke-width="2.5" fill="none" stroke-linecap="round"><circle cx="40" cy="16" r="6"/><line x1="40" y1="3" x2="40" y2="6"/><line x1="50" y1="7" x2="48" y2="9"/><line x1="54" y1="16" x2="51" y2="16"/><path d="M12 36c-6 0-8-9-1-10 1-7 10-9 14-3 3-3 11-2 11 4 7 0 7 9 1 9z" fill="#9a88a8"/><line x1="18" y1="42" x2="18" y2="42"/><line x1="24" y1="44" x2="24" y2="44"/><line x1="30" y1="42" x2="30" y2="42"/><line x1="36" y1="44" x2="36" y2="44"/></g></svg>
    <div class="weather__temp">16°<span>C</span></div>
  </div>

  <div class="criterion criterion--date">
    <div class="criterion__mark"><svg width="22" height="18" viewBox="0 0 22 18"><path d="M2 9l6 6 12-13" fill="none" stroke="#c9c6d8" stroke-width="3"/></svg></div>
    <div class="criterion__value"><b>Saturday 14</b> December</div>
  </div>
  <div class="criterion criterion--time">
    <div class="criterion__mark"><svg width="22" height="18" viewBox="0 0 22 18"><path d="M2 9l6 6 12-13" fill="none" stroke="var(--tick)" stroke-width="3"/></svg></div>
    <div class="criterion__value">11:00</div>
  </div>
  <div class="criterion criterion--place">
    <div class="criterion__mark"><svg width="22" height="18" viewBox="0 0 22 18"><path d="M2 9l6 6 12-13" fill="none" stroke="var(--tick)" stroke-width="3"/></svg></div>
    <div class="criterion__value"><b>Paris</b> France</div>
  </div>
  <div class="criterion criterion--want">
    <div class="criterion__mark"><span class="question">?</span></div>
    <div class="criterion__value"><b>You want</b></div>
  </div>

  <div class="go">GO<svg width="8" height="12" viewBox="0 0 8 12"><path d="M0 0l8 6-8 6z" fill="#4a2a40"/></svg></div>

  <footer class="bottom-bar">
    <div class="language">LANGUAGE<b>english</b></div>
    <div class="plus">PLUS<svg width="14" height="10" viewBox="0 0 14 10"><path d="M0 0h14L7 10z" fill="#fff"/></svg></div>
  </footer>
</body>
</html>
```